RW Skyline Imaging Web Site design

I am looking for a responsive single page website deign for rwskylineimages.example. This is a drone based aerial photography and cinematography business. It should have an about us section, a services section that contains photograph service, Video footage, and Aerial mapping all under the services section, a pricing section, and then a contact page for customers to contact us.

Coding

Coded - Design and coding required

Number of Pages Required

1 page

Font styles to use
Sans Serif

Colors

Designer to choose colors to be used in the design.

Requirements
Must have
• Responsive design. About us section, services section, pricing section under the services links, and contact us section, that links to a submission page where they can send Name, address, email, and comments on what they are interested in.
• See flyquad7x.example - looking for similar design.
Should not have
• clutter, or too busy design

```html
<!DOCTYPE html>
<html lang="en">
<head>
<meta charset="utf-8">
<title>RW Skyline Imaging</title>
<link href="https://fonts.googleapis.com/css2?family=Mulish:wght@400;600;700;800&family=Lato:wght@400;700&display=swap" rel="stylesheet">
<style>
:root{
  --orange:#e0861d;
  --orange-dark:#d67a12;
  --ink:#111111;
  --text:#444444;
  --white:#ffffff;
  --panel:#e9e9ea;
  --footer:#141414;
}
*{margin:0;padding:0;box-sizing:border-box}
html,body{width:1200px;height:2400px;overflow:hidden}
body{font-family:"Lato",sans-serif;color:var(--text);background:var(--white);position:relative}
.abs{position:absolute}
h1,h2,h3,.price{font-family:"Mulish",sans-serif}

/* hero */
.hero{left:0;top:0;width:1200px;height:598px;background:linear-gradient(180deg,#1d2b36 0%,#6b5a45 22%,#3d3a34 48%,#2a2b2c 75%,#3a3631 100%)}
.brand{left:228px;top:30px;width:200px;text-align:center;display:flex;align-items:center;justify-content:center;gap:8px;color:var(--white);font-family:"Mulish",sans-serif;font-size:13px;letter-spacing:3px}
.brand-dot{width:10px;height:10px;border-radius:50%;background:var(--orange)}
.nav{top:37px;display:flex;gap:0}
.nav a{position:absolute;color:var(--white);font-size:11px;text-decoration:none;white-space:nowrap}
.hero-title{left:0;top:226px;width:1200px;text-align:center;color:var(--white);font-size:26px;font-weight:800;letter-spacing:.5px}
.btn{display:flex;align-items:center;justify-content:center;font-size:10px;letter-spacing:.5px;text-transform:uppercase;text-decoration:none}
.btn-ghost{border:1px solid var(--white);color:var(--white)}
.btn-outline{border:1px solid #333;color:#333}
.btn-orange{background:var(--orange);color:var(--white)}
.btn-dark{background:var(--ink);color:var(--white)}
.social{display:flex;gap:17px}
.social span{width:12px;height:12px;border-radius:50%;background:var(--white);display:block}

/* headings */
.eyebrow{font-family:"Mulish",sans-serif;font-size:12px;font-weight:700;color:#888}
.eyebrow::before{content:"— "}
.section-title{font-size:26px;font-weight:800;color:var(--ink)}

/* about */
.about-photo{left:822px;top:598px;width:378px;height:458px;background:linear-gradient(160deg,#f1f1f2,#d9dadc 60%,#e5e5e6)}
.drone{left:672px;top:736px;width:288px;height:176px;border-radius:8px;background:radial-gradient(ellipse at center,#f4f4f4 0%,#dcdcdc 55%,rgba(220,220,220,0) 75%)}
.about-text{left:240px;top:752px;width:400px;font-size:11px;line-height:17.6px;color:#555}

/* services */
.services{left:0;top:1056px;width:1200px;height:600px;background:linear-gradient(160deg,#3b3a33 0%,#4a4430 35%,#2c2a22 65%,#1a1916 100%)}
.card{background:var(--white);text-align:center}
.card h3{font-size:16px;font-weight:800;color:var(--ink);margin-top:54px}
.card p{font-size:10.5px;line-height:17.6px;color:#555;margin:16px 27px 0}
.icon-badge{width:74px;height:74px;border-radius:50%;background:var(--white);display:flex;align-items:center;justify-content:center}

/* pricing */
.price-panel{left:0;top:1656px;width:406px;height:459px;background:linear-gradient(180deg,#ececed,#dedfe1 60%,#e6e6e7)}
.price-card{background:var(--orange);text-align:center;color:var(--white)}
.price-top{height:106px;display:flex;align-items:center;justify-content:center;border-bottom:1px solid var(--orange-dark)}
.price{font-size:38px;font-weight:600}
.price-card h3{font-size:15px;font-weight:800;margin-top:14px}
.price-card p{font-size:10px;line-height:17.6px;margin:8px 24px 0}

/* cta */
.cta{left:0;top:2115px;width:1200px;height:221px;background:var(--orange)}
.cta .eyebrow{color:#f6d3a8}
.cta-title{font-size:26px;font-weight:800;color:var(--white)}

/* footer */
.footer{left:0;top:2336px;width:1200px;height:64px;background:var(--footer)}
.copyright{left:240px;top:25px;font-size:10px;color:var(--white)}
</style>
</head>
<body>

<section class="hero abs" role="img" aria-label="Aerial photo of a city and river at sunrise under low clouds"></section>
<div class="brand abs"><span class="brand-dot"></span>RW Skyline Imaging</div>
<nav class="nav abs" style="left:0">
  <a href="#about" style="left:731px">About</a>
  <a href="#services" style="left:791px">Services</a>
  <a href="#pricing" style="left:860px">Pricing</a>
  <a href="#contact" style="left:924px">Contact</a>
</nav>
<h1 class="hero-title abs">PHOTO. VIDEO. AERIAL MAPPING.</h1>
<a class="btn btn-ghost abs" href="#about" style="left:544px;top:282px;width:112px;height:36px">Learn More</a>
<div class="social abs" style="left:874px;top:562px"><span></span><span></span><span></span></div>

<section id="about">
  <div class="about-photo abs" role="img" aria-label="Faint aerial view of city towers"></div>
  <div class="drone abs" role="img" aria-label="White quadcopter drone with orange trim and camera"></div>
  <p class="eyebrow abs" style="left:240px;top:681px">Welcome</p>
  <h2 class="section-title abs" style="left:240px;top:698px">ABOUT US</h2>
  <p class="about-text abs">Lorem ipsum dolor sit amet, consectetuer adipiscing elit, sed diam nonummy nibh euismod tincidunt ut laoreet dolore magna aliquam erat volutpat. Ut wisi enim ad minim veniam, quis nostrud exercitation ullam corper suscipit lobortis nisl ut aliquip ex ea commodo consequat. Duis autem vel eum iriure dolor in hendrerit in vulputate velit esse molestie consequat, vel illum dolore eu feugiat nulla facilisis at vero eros et accumsan et iusto odio dignissim qui blandit praesent luptatum zzril delenit augue duis dolore te feugait nulla facilisi. Nam liber tempor cum soluta nobis eleifend option congue nihil imperdiet doming id quod mazim placerat facer possim assum. Eodem modo typi, qui nunc nobis videntur parum clari, fiant sollemnes in futurum.</p>
  <a class="btn btn-outline abs" href="#services" style="left:240px;top:938px;width:101px;height:33px">Learn More</a>
</section>

<section id="services">
  <div class="services abs" role="img" aria-label="Dark mountain valley with a winding road at dusk"></div>
  <p class="eyebrow abs" style="left:0;top:1117px;width:1200px;text-align:center;color:#ccc">What we do</p>
  <h2 class="section-title abs" style="left:0;top:1134px;width:1200px;text-align:center;color:var(--white)">SERVICES</h2>

  <article class="card abs" style="left:240px;top:1245px;width:227px;height:317px">
    <h3>Photography</h3>
    <p>Lorem ipsum dolor sit amet, consectetuer adipiscing elit, sed diam nonummy nibh euismod tincidunt ut laoreet dolore magna aliquam erat volutpat. Ut wisi enim ad minim veniam, quis nostrud exerci tation ullamcorper suscipit lobortis nisl ut aliquip ex ea commodo consequat.</p>
  </article>
  <article class="card abs" style="left:486px;top:1245px;width:228px;height:317px">
    <h3>Videography</h3>
    <p>Duis autem vel eum iriure dolor in hendrerit in vulputate velit esse molestie consequat, vel praesent luptatum illum dolore eu feugiat nulla facilisis at vero eros et accumsan et iusto odio dignissim qui blandit praesent luptatum zzril delenit augue duis dolore te feugait nulla facilisi.</p>
  </article>
  <article class="card abs" style="left:733px;top:1245px;width:227px;height:317px">
    <h3>Aerial Mapping</h3>
    <p>Claritas est etiam processus dynamicus, qui sequitur mutationem quam littera consuetudium lectorum. Mirum est notare quam littera gothica, quam nunc putamus arum claram, anteposuerit litterarum formas humanitatis per seacula quarta decima et quinta decima.</p>
  </article>

  <div class="icon-badge abs" style="left:316px;top:1208px">
    <svg width="34" height="30" viewBox="0 0 34 30" fill="none" stroke="#222" stroke-width="2"><path d="M3 8h7l3-4h8l3 4h7v18H3z"/><circle cx="17" cy="16" r="6"/></svg>
  </div>
  <div class="icon-badge abs" style="left:563px;top:1208px">
    <svg width="34" height="30" viewBox="0 0 34 30" fill="none" stroke="#222" stroke-width="2"><circle cx="9" cy="7" r="4"/><circle cx="19" cy="7" r="4"/><rect x="4" y="13" width="18" height="12"/><path d="M22 17l8-4v12l-8-4"/></svg>
  </div>
  <div class="icon-badge abs" style="left:809px;top:1208px">
    <svg width="30" height="34" viewBox="0 0 30 34" fill="none" stroke="#222" stroke-width="2"><path d="M15 26s-9-9-9-15a9 9 0 0118 0c0 6-9 15-9 15z"/><circle cx="15" cy="11" r="3"/><path d="M4 31h22"/></svg>
  </div>

  <a class="btn btn-orange abs" href="#pricing" style="left:303px;top:1499px;width:101px;height:34px">Learn More</a>
  <a class="btn btn-orange abs" href="#pricing" style="left:550px;top:1499px;width:101px;height:34px">Learn More</a>
  <a class="btn btn-orange abs" href="#pricing" style="left:796px;top:1499px;width:101px;height:34px">Learn More</a>
</section>

<section id="pricing">
  <div class="price-panel abs" role="img" aria-label="Faint misty aerial view of a harbour"></div>
  <p class="eyebrow abs" style="left:0;top:1702px;width:1200px;text-align:center">Our rates</p>
  <h2 class="section-title abs" style="left:0;top:1719px;width:1200px;text-align:center">PRICING</h2>

  <article class="price-card abs" style="left:240px;top:1794px;width:227px;height:227px">
    <div class="price-top"><span class="price">$200</span></div>
    <h3>Photography</h3>
    <p>Lorem ipsum dolor sit amet, consectetuer adipiscing elit, sed diam nonummy nibh euismod.</p>
  </article>
  <article class="price-card abs" style="left:486px;top:1794px;width:228px;height:227px">
    <div class="price-top"><span class="price">$200</span></div>
    <h3>Videography</h3>
    <p>Lorem ipsum dolor sit amet, consectetuer adipiscing elit, sed diam nonummy nibh euismod.</p>
  </article>
  <article class="price-card abs" style="left:733px;top:1794px;width:227px;height:227px">
    <div class="price-top"><span class="price">$200</span></div>
    <h3>Aerial Mapping</h3>
    <p>Lorem ipsum dolor sit amet, consectetuer adipiscing elit, sed diam nonummy nibh euismod.</p>
  </article>
</section>

<section id="contact">
  <div class="cta abs"></div>
  <p class="eyebrow abs" style="left:240px;top:2203px">Get in touch</p>
  <h2 class="cta-title abs" style="left:240px;top:2221px">LIKE WHAT YOU SEE? HAVE QUESTION?</h2>
  <a class="btn btn-dark abs" href="#contact" style="left:858px;top:2221px;width:102px;height:33px">Ask Us Now</a>
</section>

<footer class="footer abs">
  <p class="copyright abs">Copyright © RW Skyline Imaging 2017</p>
  <div class="social abs" style="left:874px;top:26px"><span></span><span></span><span></span></div>
</footer>

</body>
</html>
```